Business Card Design

We are an import/export consulting business dealing with all aspects of import/export regulations. Our current design if you look at our website (www.dorvelix.com) are different country flags. It is our business to stay up to date on laws and regulations. We assist companies worldwide. We would like to keep with the flag theme but something different or maybe someone can come up with something totally different that would capture our attention. We are open to suggestions. This design then will transfer over to letterhead, our website, marketing brochures, etc.

Industry/Entity Type

Marketing

Contact Information for Business Card

Miranda J. Dorvelix, President
Dorvelix International Consultants, LLC
7 Larkmoor Lane,
Newton, NH 03791

```html
<!DOCTYPE html>
<html lang="en">
<head>
<meta charset="utf-8">
<title>Dorvelix International Consultants – Business Card</title>
<link href="https://fonts.googleapis.com/css2?family=PT+Sans:wght@400;700&display=swap" rel="stylesheet">
<style>
  :root{
    --navy:#13264c;
    --ink:#1d2f5a;
    --red:#a3202c;
    --gold:#c6a93a;
    --blue:#1f4f8f;
    --paper:#ffffff;
    --backdrop:#e9e6e1;
    --mark:#d9792a;
  }
  *{box-sizing:border-box;margin:0;padding:0}
  html,body{width:1200px;height:1000px;overflow:hidden}
  body{background:var(--backdrop);font-family:"PT Sans",sans-serif;position:relative}
  .card{position:absolute;left:290px;width:620px;height:355px;background:var(--paper);
        box-shadow:0 6px 18px rgba(0,0,0,.18);overflow:hidden}
  .card--front{top:90px}
  .card--back{top:545px}

  .brand{display:flex;align-items:center;gap:10px}
  .brand__dot{width:46px;height:46px;border-radius:50%;background:var(--mark);flex:none}
  .brand__name{color:var(--ink);font-weight:700;font-size:19px;line-height:1.05;text-transform:uppercase;letter-spacing:.5px}

  .card--front .brand{position:absolute;left:34px;top:30px}
  .flags{height:13px;background:linear-gradient(90deg,#b22234,#ffffff 12%,#d52b1e 22%,#006847 32%,#012169 42%,#ffffff 50%,#0055a4 60%,#009246 70%,#ce1126 80%,#00247d 90%,#007a4d)}
  .card--front .flags{position:absolute;right:34px;top:46px;width:210px}

  .person{position:absolute;right:36px;top:92px;text-align:right;color:var(--ink)}
  .person__name{font-size:23px;font-weight:700}
  .person__title{font-size:16px;font-weight:700;margin-top:2px}

  .stripes{position:absolute;left:0;right:0;top:158px}
  .stripe{height:5px}
  .stripe--blue{background:var(--blue)}
  .stripe--red{background:var(--red);height:6px}
  .stripe--navy{background:var(--navy);height:3px}
  .stripe--gold{background:var(--gold)}

  .contact{position:absolute;left:0;right:0;top:180px;height:120px;background:var(--navy);
           color:#fff;padding:22px 34px 0 70px;font-size:15px}
  .contact__row{display:flex;align-items:center;gap:18px;margin-bottom:10px}
  .contact__item{display:flex;align-items:center;gap:6px}
  .contact__item svg{width:12px;height:12px;fill:#fff}
  .contact__address{font-weight:700}

  .card--back .logo-block{position:absolute;left:50%;top:50%;transform:translate(-50%,-50%);
        display:flex;flex-direction:column;align-items:center;gap:12px}
  .card--back .flags{width:210px}
</style>
</head>
<body>

<section class="card card--front">
  <div class="brand">
    <span class="brand__dot"></span>
    <span class="brand__name">Dorvelix International<br>Consultants, LLC</span>
  </div>
  <div class="flags" role="img" aria-label="Row of small national flags"></div>
  <div class="person">
    <p class="person__name">Miranda J. Dorvelix</p>
    <p class="person__title">President</p>
  </div>
  <div class="stripes">
    <div class="stripe stripe--blue"></div>
    <div class="stripe stripe--red"></div>
    <div class="stripe stripe--navy"></div>
    <div class="stripe stripe--gold"></div>
  </div>
  <div class="contact">
    <div class="contact__row">
      <span class="contact__item contact__address">
        <svg viewBox="0 0 12 12"><path d="M6 1 0 6h2v5h3V8h2v3h3V6h2z"/></svg>
        7 Larkmoor Lane, Newton, NH 03791
      </span>
    </div>
    <div class="contact__row">
      <span class="contact__item">
        <svg viewBox="0 0 12 12"><path d="M2 4c0-2 2-3 4-3s4 1 4 3H8V3H4v1zM3 5h6l2 6H1z"/></svg>
        603-555-0148
      </span>
      <span class="contact__item">
        <svg viewBox="0 0 12 12"><path d="M0 2h12v8H0zm1 1v.4l5 3.3 5-3.3V3z"/></svg>
        Mirandad@dorvelix.com
      </span>
      <span class="contact__item">
        <svg viewBox="0 0 12 12"><path d="M5 7 7 5M4 6 2 8a1.5 1.5 0 0 0 2 2l2-2M8 6l2-2a1.5 1.5 0 0 0-2-2L6 4" stroke="#fff" stroke-width="1.2" fill="none"/></svg>
        www.dorvelix.com
      </span>
    </div>
  </div>
</section>

<section class="card card--back">
  <div class="logo-block">
    <div class="brand">
      <span class="brand__dot"></span>
      <span class="brand__name">Dorvelix International<br>Consultants, LLC</span>
    </div>
    <div class="flags" role="img" aria-label="Row of small national flags"></div>
  </div>
</section>

</body>
</html>
```